Harlow Crest Holdings (Remodeling company) needs a logo and business card

We need a business card design for a new company. We "flip" upmarket houses (buy, remodel and sell) in the Austin, TX area. I'd like neutral colors (grey, white, gold black). I would like it to include a simple, clean logo. Our designs are modern and uncluttered and I would like that reflected in the business card design.

Target Market(s)

Young professionals, Families, Retirees. Our properties will sell for $750k+

Industry/Entity Type

Real Estate

Contact Information for Business Card

Harlow Crets Holdings
Mona Harlow
(979) 555 0142
Owner
Rolf Tandem
(512) 555 0176
Realtor

Logo Text

Harlow Crest Holdings

Font styles to use
Serif
Script

Requirements
Must have
• Simple, classic design
Nice to have
• Clean lines, modern look
Should not have
• Too traditionally

```html
<!DOCTYPE html>
<html lang="en">
<head>
<meta charset="utf-8">
<title>Harlow Crest Holdings – Business Card</title>
<link rel="stylesheet" href="https://fonts.googleapis.com/css2?family=Open+Sans:wght@400;600&display=swap">
<style>
  :root {
    --stage: #e6e6e6;
    --gold: #fdc20e;
    --ink: #0b0b0b;
    --card-black: #050505;
    --white: #f2f2f2;
    --grey: #8a8a8a;
    --dim: #5a5a5a;
  }
  * { margin: 0; padding: 0; box-sizing: border-box; }
  html, body {
    width: 1200px; height: 1000px; overflow: hidden;
    background: var(--stage);
    font-family: "Open Sans", Arial, sans-serif;
  }
  .stage {
    width: 1200px; height: 1000px;
    display: flex; align-items: center; justify-content: center; gap: 60px;
  }
  .card {
    width: 540px; height: 303px; position: relative;
    box-shadow: 3px 4px 6px rgba(0,0,0,0.35);
  }
  /* Front */
  .card-front {
    background: var(--gold);
    display: flex; align-items: center; justify-content: center;
  }
  .brand { display: flex; align-items: center; gap: 12px; }
  .brand-mark { width: 22px; height: 22px; background: currentColor; flex: none; }
  .brand-name { font-weight: 600; white-space: nowrap; }
  .card-front .brand { color: var(--ink); }
  .card-front .brand-name { font-size: 30px; }
  /* Back */
  .card-back { background: var(--card-black); }
  .card-back .brand {
    color: var(--gold); position: absolute; left: 34px; top: 50%;
    transform: translateY(-50%); gap: 8px;
  }
  .card-back .brand-mark { width: 13px; height: 13px; }
  .card-back .brand-name { font-size: 15px; }
  .divider {
    position: absolute; left: 238px; top: 86px; width: 1px; height: 132px;
    background: linear-gradient(to bottom, transparent, rgba(253,194,14,0.55), transparent);
  }
  .contact {
    position: absolute; left: 240px; right: 0; top: 72px;
    text-align: center; color: var(--white);
  }
  .contact-name { font-size: 31px; font-weight: 400; line-height: 1; margin-bottom: 14px; }
  .contact-line {
    display: flex; align-items: center; justify-content: center; gap: 8px;
    font-size: 16px; color: var(--grey); line-height: 1.5;
  }
  .contact-line svg { width: 15px; height: 15px; fill: var(--white); }
  .contact-role { font-size: 17px; color: var(--white); margin-top: 12px; line-height: 1.3; }
  .contact-title { font-size: 13px; color: var(--dim); margin-top: 20px; }
  .accent-strip {
    position: absolute; left: 0; right: 0; bottom: 0; height: 5px; background: var(--gold);
  }
</style>
</head>
<body>
<main class="stage">
  <section class="card card-front" aria-label="Card front">
    <div class="brand">
      <span class="brand-mark"></span>
      <span class="brand-name">Harlow Crest Holdings</span>
    </div>
  </section>

  <section class="card card-back" aria-label="Card back">
    <div class="brand">
      <span class="brand-mark"></span>
      <span class="brand-name">Harlow Crest Holdings</span>
    </div>
    <div class="divider"></div>
    <div class="contact">
      <p class="contact-name">Mona Harlow</p>
      <p class="contact-line">
        <svg viewBox="0 0 24 24" aria-hidden="true"><path d="M6.6 10.8c1.4 2.8 3.8 5.1 6.6 6.6l2.2-2.2c.3-.3.7-.4 1-.2 1.1.4 2.3.6 3.6.6.6 0 1 .4 1 1V20c0 .6-.4 1-1 1C10.6 21 3 13.4 3 4c0-.6.4-1 1-1h3.5c.6 0 1 .4 1 1 0 1.3.2 2.5.6 3.6.1.3 0 .7-.2 1z"/></svg>
        (979) 555 0142
      </p>
      <p class="contact-role">Owner Rolf Tandem</p>
      <p class="contact-line">
        <svg viewBox="0 0 24 24" aria-hidden="true"><path d="M12 5C7 5 3 7 2 9.5V12h4.5V9.8c1.7-.5 3.6-.8 5.5-.8s3.8.3 5.5.8V12H22V9.5C21 7 17 5 12 5zM7 13l-3 6c0 .6.4 1 1 1h14c.6 0 1-.4 1-1l-3-6H7zm5 1.5a2.5 2.5 0 110 5 2.5 2.5 0 010-5z"/></svg>
        (512) 555 0176
      </p>
      <p class="contact-title">Realtor</p>
    </div>
    <div class="accent-strip"></div>
  </section>
</main>
</body>
</html>
```